2025 Fall Auction

Large Farm and construction online only auction November 3rd thru 5Th
Bidding Closes November 5 th at 7 pm
Now Accepting Consignment call ( 555 )-271-6038 or email Marcus@brevlandsales.com
150 + Skid Steer Attachments
50 + Pieces of farm equipment
More To Come
Consignments are welcomed Till October 25Th

Target Market(s)

New customers

```html
<!DOCTYPE html>
<html lang="en">
<head>
<meta charset="utf-8">
<title>2025 Fall Auction – Large Farm &amp; Construction</title>
<link rel="stylesheet" href="https://fonts.googleapis.com/css2?family=Oswald:wght@400;500;600&display=swap">
<style>
  :root {
    --orange: #f7931e;
    --grey: #8c8c8c;
    --grey-dark: #7a7a7a;
    --white: #ffffff;
    --backdrop: #e9e9e9;
    --photo-sky: #9fc3e6;
    --photo-shed: #b9bec4;
    --photo-ground: #8d8273;
  }
  * { box-sizing: border-box; margin: 0; padding: 0; }
  html, body { width: 1200px; height: 1001px; overflow: hidden; background: var(--backdrop); }
  body { font-family: 'Oswald', 'Arial Narrow', sans-serif; }

  .flyer-frame { position: absolute; left: 261px; top: 21px; width: 679px; height: 959px; }
  .flyer {
    position: absolute; left: 0; top: 0; width: 726px; height: 1026px;
    transform: scale(0.935); transform-origin: 0 0;
    background: var(--white); overflow: hidden;
  }

  .hero-photo {
    position: absolute; left: 0; top: 0; width: 726px; height: 372px;
    background: linear-gradient(180deg, var(--photo-sky) 0%, var(--photo-shed) 28%, #a79d8d 55%, var(--photo-ground) 100%);
  }
  .accent-band { position: absolute; left: 0; top: 362px; width: 726px; height: 10px; background: var(--orange); }
  .content-panel {
    position: absolute; left: 60px; top: 310px; width: 700px; height: 716px;
    background: var(--white); border-top-left-radius: 52px;
  }

  .brand-tab {
    position: absolute; left: 52px; top: 0; width: 194px; height: 208px;
    background: var(--white); border-radius: 0 0 22px 22px;
    display: flex; align-items: center; justify-content: center; gap: 8px;
  }
  .brand-mark { width: 16px; height: 16px; border-radius: 50%; background: var(--orange); }
  .brand-name { color: var(--orange); font-weight: 500; font-size: 26px; letter-spacing: 0.5px; text-transform: uppercase; }

  .online-badge { position: absolute; left: 528px; top: 226px; width: 172px; height: 172px; }
  .online-badge text { font-family: 'Oswald', 'Arial Narrow', sans-serif; font-weight: 500; font-size: 26px; fill: var(--white); }

  .year { position: absolute; left: 90px; top: 338px; font-size: 86px; font-weight: 500; color: var(--grey); line-height: 1; letter-spacing: -1px; }
  .fall-tag {
    position: absolute; left: 90px; top: 430px; width: 152px; height: 32px;
    background: var(--orange); color: var(--white); font-size: 24px; line-height: 32px; text-align: center;
  }
  .headline { position: absolute; left: 258px; top: 344px; color: var(--orange); font-weight: 500; font-size: 58px; line-height: 62px; text-transform: uppercase; }

  .dates-pill {
    position: absolute; left: 78px; top: 481px; width: 568px; height: 67px;
    background: var(--grey); border-radius: 8px;
    color: var(--white); font-size: 50px; font-weight: 500; line-height: 67px; text-align: center;
  }
  .closing { position: absolute; left: 78px; top: 560px; width: 568px; text-align: center; color: var(--grey); font-size: 38px; font-weight: 400; line-height: 50px; }
  .rule { position: absolute; left: 78px; top: 619px; width: 568px; height: 3px; background: var(--orange); }

  .consign-label { position: absolute; left: 92px; top: 636px; color: var(--grey); font-size: 34px; line-height: 44px; text-transform: uppercase; }
  .divider { position: absolute; left: 300px; top: 642px; width: 3px; height: 72px; background: var(--orange); }
  .contact { position: absolute; left: 318px; top: 634px; color: var(--orange); }
  .contact-line { white-space: nowrap; line-height: 46px; }
  .contact small { color: var(--grey); font-size: 19px; }
  .contact .phone { font-size: 36px; font-weight: 500; }
  .contact .email { font-size: 36px; font-weight: 500; }

  .highlights {
    position: absolute; left: 78px; top: 733px; width: 568px; height: 149px;
    background: var(--orange); border-radius: 20px; padding: 10px 0 0 36px; list-style: none;
  }
  .highlights li { display: flex; align-items: center; gap: 8px; color: var(--white); font-size: 34px; line-height: 43px; }
  .highlights svg { width: 26px; height: 26px; flex: none; }

  .deadline { position: absolute; left: 78px; top: 892px; width: 568px; text-align: center; color: var(--grey); font-size: 37px; line-height: 52px; }
  .footer-band { position: absolute; left: 0; top: 978px; width: 726px; height: 48px; background: var(--orange); }
</style>
</head>
<body>
<div class="flyer-frame">
  <div class="flyer">
    <div class="hero-photo" role="img" aria-label="Photo of skid steer attachments, a mini excavator and farm equipment lined up on gravel beside a metal building"></div>
    <div class="accent-band"></div>
    <div class="content-panel"></div>

    <div class="brand-tab">
      <span class="brand-mark"></span>
      <span class="brand-name">Brevland Sales</span>
    </div>

    <svg class="online-badge" viewBox="0 0 172 172" aria-label="Online only auction">
      <circle cx="86" cy="86" r="72" fill="var(--orange)"/>
      <circle cx="86" cy="86" r="78" fill="none" stroke="var(--orange)" stroke-width="14" stroke-dasharray="10 7"/>
      <circle cx="86" cy="86" r="62" fill="none" stroke="var(--white)" stroke-width="3"/>
      <g transform="rotate(14 86 86)" text-anchor="middle">
        <text x="86" y="62">ONLINE</text>
        <text x="86" y="92">ONLY</text>
        <text x="86" y="122">AUCTION</text>
      </g>
    </svg>

    <div class="year">2025</div>
    <div class="fall-tag">FALL AUCTION</div>
    <h1 class="headline">Large Farm<br>&amp; Construction</h1>

    <div class="dates-pill">November 3rd thru 5th</div>
    <p class="closing">Bidding Closes November 5th at 7 PM</p>
    <div class="rule"></div>

    <p class="consign-label">Now Accepting<br>Consignments</p>
    <div class="divider"></div>
    <div class="contact">
      <div class="contact-line"><small>Call </small><span class="phone">(555)-271-6038</span><small> or email</small></div>
      <div class="contact-line email">marcus@brevlandsales.com</div>
    </div>

    <ul class="highlights">
      <li><svg viewBox="0 0 24 24"><path d="M3 13l6 6L21 5" fill="none" stroke="#fff" stroke-width="3.2" stroke-linecap="round" stroke-linejoin="round"/></svg>150+ Skid Steer Attachments</li>
      <li><svg viewBox="0 0 24 24"><path d="M3 13l6 6L21 5" fill="none" stroke="#fff" stroke-width="3.2" stroke-linecap="round" stroke-linejoin="round"/></svg>50+ Pieces of Farm Equipment</li>
      <li><svg viewBox="0 0 24 24"><path d="M3 13l6 6L21 5" fill="none" stroke="#fff" stroke-width="3.2" stroke-linecap="round" stroke-linejoin="round"/></svg>More To Come!</li>
    </ul>

    <p class="deadline">Consignments welcomed till October 25th</p>
    <div class="footer-band"></div>
  </div>
</div>
</body>
</html>
```